Safety Brochure for Industry Assocations

This is an 8.5 x 11 single sided brochure for our Occupational Health and Safety Data Analytics software. If you need to use stock images we will pay for them.

Please incorporate our logo and some of the images. No need to incorporate them all. We like the idea of the boots being at the bottom of the page but we're open to other ideas.

Please note that we intend to mail this brochure to different industries so it should be generic (i.e. not construction specific).

Target Market(s)

Safety and Industry Organisations for construction, mining, forestry and oil and gas industries.

Industry/Entity Type

Industry

Font styles to use
Sans Serif

Colors

Designer to choose colors to be used in the design.

Requirements
Must have
• We are a software company that produces safety software. Our customers are companies that engage in dangerous work and use our software to improve their worker's safety. The look and feel should convey the fact that:
• -We are Big Data
• -We are Software
• -We service industry
Nice to have
• Please see the Pixlore photo of the boots. We were hoping that the desiger would be able ti modify the image with an overlay of 0's and 1's in a kind of "matrix" fashion to indicate that we are merging traditional labour work with software.
Should not have
• No medical symbols. Note that WE ARE NOT HEALTH CARE.

```html
<!DOCTYPE html>
<html lang="en">
<head>
<meta charset="utf-8">
<title>Vantex Analytics – Safety Brochure</title>
<link href="https://fonts.googleapis.com/css2?family=Open+Sans:wght@400;600;700&display=swap" rel="stylesheet">
<style>
  :root{
    --green:#45b04a;
    --green-dark:#2f8f35;
    --ink:#2b2b2b;
    --grey-strip:#4a4a4a;
    --page:#ffffff;
    --backdrop:#e8e8e8;
    --chart-bg:#f8f5ee;
    --c-purple:#8e3fa8;
    --c-green:#7cc142;
    --c-yellow:#f3d21c;
    --c-cyan:#35b7dd;
    --c-orange:#f28c28;
    --c-red:#e23b3b;
  }
  *{box-sizing:border-box;margin:0;padding:0}
  html,body{width:1200px;height:1000px;overflow:hidden;background:var(--backdrop);font-family:"Open Sans",Arial,sans-serif;color:var(--ink)}
  .brochure{position:absolute;left:237px;top:30px;width:726px;height:940px;background:var(--page);box-shadow:0 2px 10px rgba(0,0,0,.15)}
  .rule{position:absolute;left:30px;right:30px;height:2px;background:var(--green)}
  .rule--top{top:38px}
  .band-top{position:absolute;left:30px;right:30px;top:48px;height:30px;background:var(--green)}
  .logo-frame{position:absolute;left:30px;right:30px;top:78px;height:112px;border:2px solid var(--green);border-top:none;display:flex;align-items:center;padding-left:150px;gap:14px}
  .logo-dot{width:54px;height:54px;border-radius:50%;background:var(--green)}
  .logo-name{font-size:30px;font-weight:700;color:var(--ink);letter-spacing:1px}
  .headline{position:absolute;left:30px;right:30px;top:206px;height:44px;background:var(--green);color:#fff;font-size:24px;line-height:44px;padding-left:24px}
  .rule--head{top:256px}
  .checklist{position:absolute;left:60px;top:272px;list-style:none;font-size:17px;line-height:27px}
  .checklist li::before{content:"✓ ";color:var(--ink)}
  .features{position:absolute;left:30px;right:30px;top:430px;display:flex;justify-content:space-between}
  .feature{width:205px;text-align:center;font-size:15px;line-height:22px}
  .feature svg{display:block;width:205px;height:140px;margin-bottom:12px}
  .feature h2{color:var(--green);font-size:23px;font-weight:600;margin-bottom:4px}
  .feature strong{display:block;font-weight:700}
  .cta{position:absolute;left:0;top:740px;width:320px;height:170px;background:var(--green);border-right:12px solid var(--grey-strip);color:#fff;text-align:center;font-size:21px;line-height:27px;padding-top:22px;text-transform:uppercase}
  .cta span{text-transform:none;display:block}
  .boots{position:absolute;left:360px;top:700px;width:330px;height:140px;background:radial-gradient(ellipse at center,#6b4a31 0%,#4a3322 45%,#ffffff 75%)}
  .contact{position:absolute;right:40px;top:856px;text-align:right;font-size:19px;line-height:28px;letter-spacing:.5px}
</style>
</head>
<body>
<main class="brochure">
  <div class="rule rule--top"></div>
  <div class="band-top"></div>
  <header class="logo-frame">
    <div class="logo-dot"></div>
    <div class="logo-name">Vantex Analytics</div>
  </header>
  <h1 class="headline">Leverage the power of BIG DATA!</h1>
  <div class="rule rule--head"></div>
  <ul class="checklist">
    <li>LEAD the next wave of injury reduction</li>
    <li>ENGAGE with members through collaboration and benchmarking</li>
    <li>PROMOTE standardization</li>
    <li>ANALYZE Accurate, Timely and Complete Leading Indicators</li>
    <li>TRAIN industry more proactively</li>
  </ul>

  <section class="features">
    <article class="feature">
      <svg viewBox="0 0 205 140" aria-label="Stacked bar chart">
        <rect width="205" height="140" fill="var(--chart-bg)"/>
        <text x="102" y="14" font-size="8" text-anchor="middle" fill="#555">Training Hours</text>
        <line x1="20" y1="120" x2="195" y2="120" stroke="#999"/>
        <g>
          <rect x="30" y="95" width="20" height="25" fill="var(--c-purple)"/><rect x="30" y="80" width="20" height="15" fill="var(--c-green)"/><rect x="30" y="70" width="20" height="10" fill="var(--c-cyan)"/>
          <rect x="62" y="92" width="20" height="28" fill="var(--c-yellow)"/><rect x="62" y="72" width="20" height="20" fill="var(--c-green)"/><rect x="62" y="60" width="20" height="12" fill="var(--c-cyan)"/>
          <rect x="94" y="98" width="20" height="22" fill="var(--c-orange)"/><rect x="94" y="78" width="20" height="20" fill="var(--c-purple)"/><rect x="94" y="66" width="20" height="12" fill="var(--c-green)"/>
          <rect x="126" y="90" width="20" height="30" fill="var(--c-purple)"/><rect x="126" y="68" width="20" height="22" fill="var(--c-yellow)"/><rect x="126" y="50" width="20" height="18" fill="var(--c-cyan)"/>
          <rect x="158" y="96" width="20" height="24" fill="var(--c-red)"/><rect x="158" y="72" width="20" height="24" fill="var(--c-purple)"/><rect x="158" y="44" width="20" height="28" fill="var(--c-cyan)"/>
        </g>
      </svg>
      <h2>Training</h2>
      <p>Analyze needs of Industry<br>Deliver Proactive Training</p>
      <strong>Improve Safety</strong>
    </article>

    <article class="feature">
      <svg viewBox="0 0 205 140" aria-label="Pie chart">
        <rect width="205" height="140" fill="var(--chart-bg)"/>
        <text x="102" y="14" font-size="8" text-anchor="middle" fill="#555">Incidents by Type</text>
        <g transform="translate(102,78)">
          <path d="M0 0 L0 -42 A42 42 0 0 1 40 -13 Z" fill="var(--c-cyan)"/>
          <path d="M0 0 L40 -13 A42 42 0 0 1 30 29 Z" fill="var(--c-yellow)"/>
          <path d="M0 0 L30 29 A42 42 0 0 1 18 38 Z" fill="var(--c-green)"/>
          <path d="M0 0 L18 38 A42 42 0 1 1 0 -42 Z" fill="var(--c-red)"/>
        </g>
      </svg>
      <h2>Benchmarking</h2>
      <p>Engage with Members<br>Promote Collaborative<br>Advancement of Safety</p>
      <strong>Improve Safety</strong>
    </article>

    <article class="feature">
      <svg viewBox="0 0 205 140" aria-label="Grouped bar chart">
        <rect width="205" height="140" fill="var(--chart-bg)"/>
        <text x="102" y="14" font-size="8" text-anchor="middle" fill="#555">Observations</text>
        <line x1="15" y1="110" x2="195" y2="110" stroke="#999"/>
        <g>
          <rect x="22" y="70" width="8" height="40" fill="var(--c-purple)"/><rect x="31" y="85" width="8" height="25" fill="var(--c-red)"/><rect x="40" y="92" width="8" height="18" fill="var(--c-yellow)"/>
          <rect x="56" y="60" width="8" height="50" fill="var(--c-green)"/><rect x="65" y="80" width="8" height="30" fill="var(--c-purple)"/><rect x="74" y="88" width="8" height="22" fill="var(--c-red)"/>
          <rect x="90" y="66" width="8" height="44" fill="var(--c-red)"/><rect x="99" y="76" width="8" height="34" fill="var(--c-cyan)"/><rect x="108" y="90" width="8" height="20" fill="var(--c-yellow)"/>
          <rect x="124" y="50" width="8" height="60" fill="var(--c-purple)"/><rect x="133" y="72" width="8" height="38" fill="var(--c-green)"/><rect x="142" y="84" width="8" height="26" fill="var(--c-red)"/>
          <rect x="158" y="40" width="8" height="70" fill="var(--c-red)"/><rect x="167" y="58" width="8" height="52" fill="var(--c-purple)"/><rect x="176" y="78" width="8" height="32" fill="var(--c-cyan)"/>
        </g>
        <g>
          <rect x="40" y="122" width="14" height="6" fill="var(--c-yellow)"/><rect x="90" y="122" width="14" height="6" fill="var(--c-green)"/><rect x="140" y="122" width="14" height="6" fill="var(--c-red)"/>
        </g>
      </svg>
      <h2>Trend Analysis</h2>
      <p>Monitor Industry Trends<br>Implement Corrective Initiatives</p>
      <strong>Improve Safety</strong>
    </article>
  </section>

  <div class="cta">The next<br>big step<br>in injury<br>reduction!<span>For your entire industry</span></div>
  <div class="boots" role="img" aria-label="Photo of worn leather work boots standing on soil"></div>
  <div class="contact">1-888-555-0142<br>www.vantexanalytics.com</div>
</main>
</body>
</html>
```